Hotel Company Personal Business Card

This is a hotel business, personal business card. Need it sleek, professional, and sharp looking. I have a design attached that we can work with. My turnaround time is April 8th. I would need the cards by then. One side only color, the other side all details. This is flexible depending on the designs you come up with. I would like a boutique, unique, modern type of touch to the business card. Memorable type of card that people will want to keep.

Target Market(s)

Business professionals

Industry/Entity Type

Hospitality/Hotels & Resorts

Contact Information for Business Card

Name, email, phone number, address, and company name. Anything unique

Font styles to use
Serif
Sans Serif

Colors

Designer to choose colors to be used in the design.

Requirements
Nice to have
• Neutral colors. Eye popping logo. Sleek design. Boutique feel. Hint of color.

```html
<!DOCTYPE html>
<html lang="en">
<head>
<meta charset="utf-8">
<title>Harborline Hotel – Business Card</title>
<link rel="stylesheet" href="https://fonts.googleapis.com/css2?family=Playfair+Display:wght@400;600;700&display=swap">
<style>
  :root {
    --navy: #163a56;
    --white: #ffffff;
    --paper: #fbfbfb;
    --ink: #163a56;
    --backdrop: #2a2c2f;
    --photo-sky: #eef3f7;
    --photo-water: #c9d8e4;
    --photo-sand: #d8c3a2;
    --wave: #ececec;
  }
  * { box-sizing: border-box; margin: 0; padding: 0; }
  html, body { width: 1200px; height: 952px; overflow: hidden; }
  body {
    background: var(--backdrop);
    font-family: "Playfair Display", Georgia, serif;
    position: relative;
  }
  .card {
    position: absolute;
    left: 280px;
    width: 640px;
    height: 366px;
    overflow: hidden;
    box-shadow: 0 14px 34px rgba(0,0,0,.45);
  }
  .card--front { top: 80px; background: var(--navy); }
  .card--back { top: 506px; background: var(--paper); }

  /* Front */
  .front-photo {
    position: absolute; left: 0; top: 0; width: 100%; height: 200px;
    background: linear-gradient(120deg, var(--photo-sky) 0%, var(--white) 30%, var(--photo-water) 60%, var(--photo-sand) 82%, var(--photo-sky) 100%);
  }
  .front-band {
    position: absolute; left: 0; top: 200px; width: 100%; height: 166px;
    display: flex; align-items: center; justify-content: center; gap: 18px;
  }
  .brand-square {
    width: 44px; height: 44px;
    border: 1.5px solid var(--white); border-radius: 6px;
  }
  .brand-name {
    color: var(--white); font-size: 40px; font-weight: 600; letter-spacing: .5px;
  }

  /* Back */
  .back-wave {
    position: absolute; right: 0; bottom: 0; width: 430px; height: 190px;
    background: radial-gradient(ellipse at 60% 80%, var(--wave) 0%, rgba(236,236,236,0) 70%);
  }
  .contact-rail {
    position: absolute; left: 44px; top: 112px; width: 62px; bottom: 0;
    background: var(--navy); border-radius: 31px 31px 0 0;
    display: flex; flex-direction: column; align-items: center;
    padding-top: 34px; gap: 22px;
  }
  .contact-rail svg { width: 20px; height: 20px; }
  .contact-details {
    position: absolute; left: 128px; top: 136px; color: var(--ink);
  }
  .person-name { font-size: 30px; font-weight: 700; margin-bottom: 14px; }
  .contact-line { font-size: 15px; line-height: 1; margin-bottom: 24px; }
  .back-brand {
    position: absolute; right: 40px; top: 150px;
    display: flex; align-items: center; gap: 14px;
  }
  .back-brand .brand-square { border-color: var(--navy); width: 38px; height: 38px; }
  .back-brand .brand-name { color: var(--navy); font-size: 28px; font-weight: 700; }
</style>
</head>
<body>
  <section class="card card--front" aria-label="Card front">
    <div class="front-photo" role="img" aria-label="Photo of a bright hotel poolside terrace with parasols and loungers"></div>
    <div class="front-band">
      <span class="brand-square"></span>
      <span class="brand-name">Harborline Hotel</span>
    </div>
  </section>

  <section class="card card--back" aria-label="Card back">
    <div class="back-wave" role="img" aria-label="Faint flowing line pattern and leaf shadow"></div>
    <div class="contact-rail">
      <svg viewBox="0 0 20 20" aria-hidden="true"><circle cx="10" cy="6" r="4" fill="#fff"/><path d="M2 19c0-5 4-7 8-7s8 2 8 7z" fill="#fff"/></svg>
      <svg viewBox="0 0 20 20" aria-hidden="true" fill="none" stroke="#fff" stroke-width="1.3"><rect x="2" y="4" width="16" height="12"/><path d="M2 4l8 7 8-7M2 16l6-6M18 16l-6-6"/></svg>
      <svg viewBox="0 0 20 20" aria-hidden="true" fill="none" stroke="#fff" stroke-width="1.3"><path d="M5 2l3 4-2 2c1 2 3 4 5 5l2-2 4 3-2 3C9 17 3 11 2 5z"/><path d="M12 3a5 5 0 0 1 5 5M12 6a2 2 0 0 1 2 2"/></svg>
      <svg viewBox="0 0 20 20" aria-hidden="true" fill="none" stroke="#fff" stroke-width="1.3"><circle cx="10" cy="10" r="8"/><ellipse cx="10" cy="10" rx="3.5" ry="8"/><path d="M2 10h16M3.5 6h13M3.5 14h13"/></svg>
    </div>
    <div class="contact-details">
      <p class="person-name">Ellis Marlow</p>
      <p class="contact-line">ellis@harborlinehotel.com</p>
      <p class="contact-line">(55) 4821 7390</p>
      <p class="contact-line">www.harborlinehotel.com</p>
    </div>
    <div class="back-brand">
      <span class="brand-square"></span>
      <span class="brand-name">Harborline Hotel</span>
    </div>
  </section>
</body>
</html>
```